Business Cards

Business cards (double-sided) to be handed out to clients and potential clients, with contact details, logo .

Target Market(s)

Small to medium size businesses

Industry/Entity Type

Accountants

Contact Information for Business Card

Brightmere Ledger Accounting & Advisory Ltd

Colors

Designer to choose only greyscale colors for use in the design.

Requirements
Must have
• Name, Title, Address, Phone number, Email, Website
Nice to have
• Modern, clean lines, classy
Should not have
• Business cards to be double-sided. Form keeps reverting to single-sided.

```html
<!DOCTYPE html>
<html lang="en">
<head>
<meta charset="utf-8">
<title>Brightmere Ledger – Business Card</title>
<link href="https://fonts.googleapis.com/css2?family=Montserrat:wght@400;500;700&display=swap" rel="stylesheet">
<style>
  :root {
    --stage: #1c1c1c;
    --card-dark: #2f2f2f;
    --card-light: #ffffff;
    --ink: #2b2b2b;
    --ink-soft: #4a4a4a;
    --rule: #6a6a6a;
    --silver: #b9b9b9;
    --tab: #444444;
  }
  * { margin: 0; padding: 0; box-sizing: border-box; }
  html, body { width: 1200px; height: 852px; overflow: hidden; }
  body {
    background: var(--stage);
    font-family: "Montserrat", sans-serif;
    color: var(--ink);
    display: flex;
    flex-direction: column;
    align-items: center;
    justify-content: center;
    gap: 44px;
  }
  .card {
    width: 630px;
    height: 360px;
    position: relative;
    box-shadow: 0 10px 30px rgba(0,0,0,0.5);
  }
  .card--back {
    background: var(--card-dark);
    display: flex;
    align-items: center;
    justify-content: center;
  }
  .brand {
    display: flex;
    align-items: center;
    gap: 10px;
    font-weight: 500;
    text-transform: uppercase;
    letter-spacing: 0.12em;
  }
  .brand__mark { width: 12px; height: 12px; background: currentColor; }
  .card--back .brand { color: var(--silver); font-size: 28px; }

  .card--front { background: var(--card-light); }
  .card--front .brand {
    position: absolute; left: 40px; top: 68px;
    color: var(--ink); font-size: 15px;
  }
  .holder {
    position: absolute; right: 48px; top: 46px; text-align: right;
  }
  .holder__name { font-weight: 700; font-size: 24px; letter-spacing: 0.01em; color: var(--ink-soft); }
  .holder__title { font-size: 13px; letter-spacing: 0.08em; color: var(--ink-soft); margin-top: 2px; }
  .tab {
    position: absolute; right: 0; top: 40px; width: 12px; height: 42px; background: var(--tab);
  }
  .rule {
    position: absolute; left: 160px; right: 42px; top: 138px;
    height: 1px; background: var(--rule);
  }
  .address {
    position: absolute; right: 48px; top: 160px; text-align: right;
    font-size: 13px; line-height: 1.5; color: var(--ink-soft);
  }
  .contact {
    position: absolute; left: 160px; bottom: 40px;
    list-style: none; font-size: 13px; line-height: 1.7; color: var(--ink-soft);
  }
  .contact li { display: flex; align-items: center; gap: 8px; }
  .contact svg { width: 11px; height: 11px; flex: none; }
</style>
</head>
<body>
  <section class="card card--back">
    <div class="brand"><span class="brand__mark"></span>Brightmere Ledger</div>
  </section>

  <section class="card card--front">
    <div class="brand"><span class="brand__mark"></span>Brightmere Ledger</div>
    <span class="tab"></span>
    <div class="holder">
      <p class="holder__name">DANIEL HARLOW</p>
      <p class="holder__title">DIRECTOR</p>
    </div>
    <div class="rule"></div>
    <address class="address" style="font-style:normal">
      Suite 4120 PMB 70318<br>Minneapolis, MN 55402
    </address>
    <ul class="contact">
      <li>
        <svg viewBox="0 0 12 12" aria-hidden="true"><path d="M2.5 1h2l1 3-1.3 1a6 6 0 0 0 2.8 2.8l1-1.3 3 1v2a1 1 0 0 1-1 1A9.5 9.5 0 0 1 1.5 2a1 1 0 0 1 1-1z" fill="#4a4a4a"/></svg>
        (952) 555-0148
      </li>
      <li>
        <svg viewBox="0 0 12 12" aria-hidden="true"><rect x="1" y="2.5" width="10" height="7" fill="none" stroke="#4a4a4a" stroke-width="1.2"/><path d="M1 2.5l5 4 5-4" fill="none" stroke="#4a4a4a" stroke-width="1.2"/></svg>
        hello@brightmereledger.com
      </li>
      <li>
        <svg viewBox="0 0 12 12" aria-hidden="true"><circle cx="6" cy="6" r="5" fill="none" stroke="#4a4a4a" stroke-width="1.1"/><path d="M1 6h10M6 1c-2 2.5-2 7.5 0 10M6 1c2 2.5 2 7.5 0 10" fill="none" stroke="#4a4a4a" stroke-width="0.9"/></svg>
        www.brightmereledger.com
      </li>
    </ul>
  </section>
</body>
</html>
```